International travel site frontpage redesign

We sell tours to Scandinavia through our website www.brightfell-journeys.com. The website has become a bit old fashioned and we are in the process of making the website responsive. As you can see from the attached pictures the website will be wider with the responsive design, and our current design does not fit anymore.

Here is what we are looking for:
- A website that reflects a trustworthy and quality oriented company.
- Making the website more modern looking, but still recognisable (we want to keep the colours).
- keeping in mind that the age group of our customers are from 20-80 years old (most in their 60s).
- We want to remove the popular tours part and are instead looking to replace this with picture boxes the following subjects Scandinavia Specialist, Special Offers, Contact, Norway (or Norway Tours), Sweden (or Sweden Tours), Iceland (or Iceland Tours), Combination Tours. Possibly also Lapland, Winter, Northern Lights, Fjords and Capitals. Some of these categories can be smaller or perhaps half boxes; i.e. Winter and Northern lights in one. If we end up with four boxes per line perhaps we could add a social media box next to the three first ones.
- The above means that the left hand meny with Norway Tours, Sweden Tours etc will be redundant.
- we will add another line to the search Box (on the top): Destinations
- The top menu will have the same categories, but we need to add languages as the website will be in English and German.
- The footer must be changed
- We can take away the box to the right where it says "your window to booking the best of our world"

Target Market(s)

Travelling to Scandinavia is not low cost, so the website needs to appeal to those that can afford to travel to our destination.
The age group of our customers are from 20-80 years old (most in their 60s).

Industry/Entity Type

Travel

Number of Pages Required

1 page

Requirements
Should not have
• Flashy or cheap looking special offers...

```html
<!DOCTYPE html>
<html lang="en">
<head>
<meta charset="utf-8">
<title>Brightfell Journeys – Tours to Scandinavia</title>
<link href="https://fonts.googleapis.com/css2?family=Ubuntu:wght@300;400;500;700&display=swap" rel="stylesheet">
<style>
:root{
  --page:#efefef;
  --panel:#ffffff;
  --line:#dcdcdc;
  --ink:#2b2b2b;
  --muted:#555;
  --soft:#777;
  --red:#c8141b;
  --red-dark:#9e0d12;
  --green:#2f8a1c;
  --orange:#e5601a;
  --blue:#1a7fd8;
  --dark:#1e1e1e;
}
*{box-sizing:border-box;margin:0;padding:0}
html,body{width:1053px;height:1200px;overflow:hidden;background:var(--page)}
body{font-family:"Ubuntu",sans-serif;color:var(--ink)}
.stage{position:absolute;left:0;top:0;width:1230px;height:1401px;transform:scale(0.8561);transform-origin:0 0}
.abs{position:absolute}

/* header */
.lang-label{left:765px;top:19px;font-size:16px;color:var(--muted)}
.lang-select{left:848px;top:15px;width:100px;height:29px;background:#fff;border:1px solid var(--line);border-radius:3px;font-size:13px;display:flex;align-items:center;gap:7px;padding-left:11px;color:#333}
.lang-select .flag{width:16px;height:11px;background:linear-gradient(#fff 40%,var(--red) 40% 60%,#fff 60%);border:1px solid #23408e}
.phone{left:963px;top:18px;font-size:19px;color:#444;display:flex;align-items:center;gap:6px}
.logo{left:104px;top:62px;display:flex;align-items:center;gap:12px;font-size:26px;font-weight:300;letter-spacing:1.5px;color:#6b6b6b;text-transform:uppercase}
.logo .mark{width:18px;height:18px;border-radius:50%;background:var(--red)}
.nav a{position:absolute;top:62px;height:36px;display:flex;align-items:center;justify-content:center;font-size:13px;font-weight:700;color:#333;text-decoration:none;background:linear-gradient(#fafafa,#dedede);border:1px solid #d0d0d0;border-radius:3px;box-shadow:0 2px 3px rgba(0,0,0,.12)}
.nav a.active{background:linear-gradient(#6a6a6a,#3f3f3f);color:#fff;border-color:#444}

/* search */
.search{left:105px;top:118px;width:181px;height:398px;background:var(--panel);border-radius:12px;overflow:hidden;box-shadow:0 1px 3px rgba(0,0,0,.08)}
.search h2{height:36px;background:linear-gradient(#d9161d,var(--red-dark));color:#fff;font-size:17px;font-weight:500;padding:8px 17px}
.search label{position:absolute;left:15px;font-size:13px;color:#333}
.search .field{position:absolute;left:15px;width:150px;height:29px;border:1px solid #ccc;border-radius:3px;font-size:12px;color:#999;padding:7px 12px}
.search .field.sel::after{content:"";position:absolute;right:8px;top:10px;border:3px solid transparent;border-top-color:#666;margin-top:5px}
.search .field.sel::before{content:"";position:absolute;right:8px;top:6px;border:3px solid transparent;border-bottom-color:#666}
.search .go{position:absolute;left:15px;top:349px;width:150px;height:37px;background:linear-gradient(#3aa524,#23771a);border-radius:3px;color:#fff;font-size:15px;display:flex;align-items:center;justify-content:center}

.hero{left:305px;top:119px;width:622px;height:397px;border-radius:14px;overflow:hidden;background:linear-gradient(180deg,#1b6fd0 0%,#5aa2e6 18%,#3f6e3a 38%,#66b3a8 52%,#d9e2e4 66%,#8aa35a 82%,#4d7a2c 100%)}
.hero .slider{position:absolute;right:-28px;bottom:-28px;width:110px;height:110px;border-radius:50%;background:var(--blue)}

.aside{left:943px;top:120px;width:181px;height:396px;background:var(--panel);border-radius:12px;box-shadow:0 1px 3px rgba(0,0,0,.08)}
.aside .tag{position:absolute;left:21px;top:20px;font-size:15.5px;line-height:28px;color:#333}
.aside .tag b{color:var(--red);font-size:21px;font-weight:500}
.feature{position:absolute;left:16px;width:151px;height:77px;border:1px solid #d4d4d4;border-radius:3px;background:linear-gradient(#fff,#f2f2f2);display:flex;align-items:center;gap:12px;padding-left:13px;font-size:15px;line-height:21px}
.feature strong{font-weight:700;display:block}

/* welcome */
.welcome{left:105px;top:533px;width:1019px;height:366px;background:var(--panel);border:1px solid var(--line);border-radius:12px;overflow:hidden}
.welcome h1{height:40px;background:linear-gradient(#111,#444 60%,#777);color:#fff;font-size:19px;font-weight:500;padding:8px 25px}
.card{position:absolute;top:60px;width:477px;height:152px;background:#ececec}
.card .photo{position:absolute;left:0;top:0;width:226px;height:152px}
.card h3{position:absolute;left:248px;top:14px;font-size:15px;font-weight:500}
.card p{position:absolute;left:248px;top:37px;width:225px;font-size:12.5px;line-height:21px;color:#555;white-space:nowrap}
.card .btn{position:absolute;left:247px;top:110px;width:95px;height:28px;background:linear-gradient(#f07027,#d2500e);border-radius:3px;color:#fff;font-size:12.5px;display:flex;align-items:center;justify-content:center}
.badge{position:absolute;left:953px;top:51px;width:50px;height:50px;border-radius:50%;background:radial-gradient(#ffb020,#f08a00);border:2px dashed #ffd15c}
.tile{position:absolute;top:230px;width:111px;height:111px;overflow:hidden}
.tile span{position:absolute;left:10px;bottom:5px;color:#fff;font-size:14.5px;line-height:17px;text-shadow:0 1px 2px rgba(0,0,0,.6)}
.tile::before{content:"";position:absolute;left:0;right:0;bottom:0;height:44px;background:rgba(0,0,0,.35)}
.tile i{position:absolute;right:2px;bottom:2px;width:12px;height:12px;background:var(--red)}
.tile i::after{content:"";position:absolute;left:4px;top:3px;border:3px solid transparent;border-left:4px solid #fff}

.quick{position:absolute;top:913px;width:242px;height:47px;background:var(--panel);border:1px solid var(--line);border-radius:14px;display:flex;align-items:center;gap:12px;padding-left:20px;font-size:16px;color:#222}
.quick b{font-weight:700}

.footer{left:105px;top:977px;width:1019px;height:327px;background:var(--panel);border:1px solid var(--line);border-radius:12px}
.col{position:absolute}
.col h4{font-size:14.5px;font-weight:500;color:#333;margin-bottom:6px}
.col li{list-style:none;font-size:11.5px;color:#555;line-height:24px;white-space:nowrap}
.copy{left:0;width:1230px;top:1318px;text-align:center;font-size:11.5px;color:#555}
.pay{top:1353px;height:28px;border-radius:2px}
.social{left:681px;top:1344px;width:144px;height:44px;border:1px solid #bbb;background:linear-gradient(#fff,#e9e9e9);border-radius:2px}
.social::before{content:"";position:absolute;left:5px;top:5px;width:32px;height:32px;background:#3b5998;border-radius:2px}
</style>
</head>
<body>
<div class="stage">

  <div class="abs lang-label">Language</div>
  <div class="abs lang-select"><span class="flag"></span>English ▾</div>
  <div class="abs phone">
    <svg width="22" height="18" viewBox="0 0 22 18"><path d="M2 6c0-3 4-5 9-5s9 2 9 5l-4 1-1-3H7L6 7Z" fill="#555"/><rect x="4" y="8" width="14" height="9" rx="2" fill="#555"/><circle cx="11" cy="12.5" r="2.5" fill="#fff"/></svg>
    +47 21 00 48 62
  </div>

  <div class="abs logo">Brightfell <span class="mark"></span> Journeys</div>

  <nav class="nav">
    <a class="active" style="left:504px;width:79px">HOME</a>
    <a style="left:591px;width:87px">FJORDS</a>
    <a style="left:686px;width:124px">CAPITALS</a>
    <a style="left:818px;width:103px">CRUISES</a>
    <a style="left:930px;width:84px">WINTER</a>
    <a style="left:1023px;width:101px">PICTURES</a>
  </nav>

  <form class="abs search">
    <h2>Search</h2>
    <label style="top:49px">All tour type</label>
    <div class="field sel" style="top:71px">Select</div>
    <label style="top:108px">Destination</label>
    <div class="field sel" style="top:130px">Select</div>
    <label style="top:170px">All tour selections</label>
    <div class="field sel" style="top:193px">Select</div>
    <label style="top:230px">All travel periods</label>
    <div class="field sel" style="top:253px">Select</div>
    <label style="top:288px">Free Search</label>
    <div class="field" style="top:310px">Search</div>
    <div class="go">Search</div>
  </form>

  <div class="abs hero" role="img" aria-label="Traveller sitting on a white sand beach below green mountains beside a turquoise bay">
    <div class="slider">
      <svg class="abs" style="left:27px;top:33px" width="42" height="26" viewBox="0 0 42 26"><path d="M12 2 2 13l10 11M30 2l10 11-10 11" stroke="#fff" stroke-width="2.5" fill="none"/></svg>
    </div>
  </div>

  <aside class="abs aside">
    <p class="tag">Your window to<br>booking <b>the best</b><br>of our <b>world</b></p>
    <div class="feature" style="top:114px">
      <svg width="32" height="26" viewBox="0 0 32 26"><rect x="1" y="1" width="30" height="24" fill="none" stroke="#666" stroke-width="1.5"/><path d="M4 21l8-9 6 6 4-4 6 7Z" fill="none" stroke="#666" stroke-width="1.5"/><circle cx="23" cy="7" r="2" fill="#666"/></svg>
      <div><strong>Spectacular</strong>Scenery</div>
    </div>
    <div class="feature" style="top:204px">
      <svg width="32" height="28" viewBox="0 0 32 28"><circle cx="9" cy="6" r="3" fill="none" stroke="#666" stroke-width="1.5"/><circle cx="18" cy="5" r="3" fill="none" stroke="#666" stroke-width="1.5"/><circle cx="26" cy="6" r="3" fill="none" stroke="#666" stroke-width="1.5"/><path d="M4 27V14h8v6h10v7" fill="none" stroke="#666" stroke-width="1.5"/></svg>
      <div><strong>Traditional</strong>Culture</div>
    </div>
    <div class="feature" style="top:294px">
      <svg width="32" height="20" viewBox="0 0 32 20"><path d="M3 2v16M1 2v5c0 2 4 2 4 0V2M29 2v16M29 2c-3 2-3 7 0 8" stroke="#666" stroke-width="1.8" fill="none"/><circle cx="16" cy="10" r="7" fill="none" stroke="#666" stroke-width="1.8"/><circle cx="16" cy="10" r="3" fill="#666"/></svg>
      <div><strong>Culinary</strong>Delights</div>
    </div>
  </aside>

  <section class="abs welcome">
    <h1>Welcome Scandinavia</h1>
    <article class="card" style="left:24px">
      <div class="photo" role="img" aria-label="Hiker with a red backpack looking over a fjord" style="background:linear-gradient(#3f8fd6,#a9cbe8 40%,#5c6a6e 65%,#2c4e6a)"></div>
      <h3>Scandinavia Specialist</h3>
      <p>Lorem Ipsum is simply dummy text<br>of the printing and typesetting<br>industry. Lorem Ipsum has been .</p>
      <div class="btn">Click Here</div>
    </article>
    <article class="card" style="left:519px">
      <div class="photo" role="img" aria-label="Mountains reflected in a calm blue harbour" style="background:linear-gradient(#8fbfe6,#cfe2ee 30%,#5b6e5e 50%,#5fb0e0 70%,#1d6fb8)"></div>
      <h3>Special Offers</h3>
      <p>Lorem Ipsum is simply dummy text<br>of the printing and typesetting<br>industry. Lorem Ipsum has been .</p>
      <div class="btn">Click Here</div>
    </article>
    <div class="badge" role="img" aria-label="Special offers badge"></div>

    <div class="tile" role="img" aria-label="Norway tours, mountains at sunset" style="left:24px;background:linear-gradient(#6b4d8a,#e67d4a 45%,#3a3f5c)"><span>Norway<br>Tours</span><i></i></div>
    <div class="tile" role="img" aria-label="Sweden tours, child by the water" style="left:147px;background:linear-gradient(#3e7fc0,#9cbfdb 50%,#2a5c90)"><span>Sweden<br>Tours</span><i></i></div>
    <div class="tile" role="img" aria-label="Iceland tours, glacier lagoon" style="left:269px;background:linear-gradient(#7fa8c8,#e8eef2 50%,#3e5666)"><span>Iceland<br>Tours</span><i></i></div>
    <div class="tile" role="img" aria-label="Combination tours, old town waterfront" style="left:392px;background:linear-gradient(#8fa37a,#c9b89a 50%,#5f6e4d)"><span>Combination<br>Tours</span><i></i></div>
    <div class="tile" role="img" aria-label="Lapland tours, group jumping on a hilltop" style="left:515px;background:linear-gradient(#6a9ccc,#b7d0e4 55%,#4b5a45)"><span>Lapland<br>Tours</span><i></i></div>
    <div class="tile" role="img" aria-label="Winter tours, snow activities" style="left:638px;background:linear-gradient(#2d72c4,#dfe8f2 55%,#a53c6a)"><span>Winter<br>Tours</span><i></i></div>
    <div class="tile" role="img" aria-label="Northern lights over snowy forest" style="left:760px;background:linear-gradient(#0c3355,#2fc48a 45%,#0f3a5c)"><span>Northern<br>Lights</span><i></i></div>
    <div class="tile" role="img" aria-label="Fjords and capitals, waterfront houses" style="left:883px;background:linear-gradient(#5c8cc0,#7da35a 50%,#2e5a2a)"><span>Fjords &amp;<br>Capitals</span><i></i></div>
  </section>

  <div class="quick" style="left:105px">
    <svg width="34" height="26" viewBox="0 0 34 26"><circle cx="12" cy="7" r="6" fill="#777"/><path d="M1 26c0-8 5-12 11-12s11 4 11 12Z" fill="#777"/><rect x="24" y="9" width="9" height="8" rx="1" fill="#777"/><path d="M26 9V6a2.5 2.5 0 0 1 5 0v3" stroke="#777" stroke-width="1.6" fill="none"/></svg>
    <span><b>Customer</b> Protection</span>
  </div>
  <div class="quick" style="left:364px">
    <svg width="30" height="28" viewBox="0 0 30 28"><path d="M1 13a14 12 0 0 1 28 0Z" fill="#777"/><path d="M15 13v11a3 3 0 0 1-6 0" stroke="#777" stroke-width="2" fill="none"/></svg>
    <span><b>Travel</b> Insurance</span>
  </div>
  <div class="quick" style="left:623px">
    <svg width="28" height="28" viewBox="0 0 28 28"><path d="M14 20S7 13 7 8a7 7 0 0 1 14 0c0 5-7 12-7 12Z" fill="none" stroke="#777" stroke-width="1.8"/><circle cx="14" cy="8" r="2.5" fill="#777"/><path d="M3 19l-2 8h26l-2-8" fill="none" stroke="#777" stroke-width="1.8"/></svg>
    <span><b>Travel</b> Experiences</span>
  </div>
  <div class="quick" style="left:882px">
    <svg width="26" height="28" viewBox="0 0 26 28"><path d="M2 2h22v20H12l-6 5v-5H2Z" fill="#777"/><text x="13" y="18" font-family="Ubuntu,sans-serif" font-size="15" font-weight="700" fill="#fff" text-anchor="middle">?</text></svg>
    <span><b>Customer</b> Service/FAQ</span>
  </div>

  <footer class="abs footer">
    <div class="col" style="left:20px;top:20px"><h4>Tour Types</h4><ul><li>Escorted Coach Tours</li><li>Independent Rail Tours</li><li>Independent Short Breaks</li><li>Partly Escorted Tours</li><li>Scandinavian Cruises</li><li>Self Drive Tours</li></ul></div>
    <div class="col" style="left:202px;top:20px"><h4>Winter Tour Types</h4><ul><li>Norway Winter Tours</li><li>Sweden Winter Tours</li><li>Finland Winter Tours</li><li>Iceland Winter Tours</li></ul></div>
    <div class="col" style="left:376px;top:24px"><h4>Recently Updated Tours</h4><ul><li>Lapland Winter Adventure</li><li>Treetop Lodge, Northern Lights &amp; Tromsø</li><li>Snow Lodge, Northern Lights &amp; Coastal Voyage</li></ul></div>
    <div class="col" style="left:619px;top:24px"><h4>Tour Selections</h4><ul><li>Fjord Tours</li><li>Scandinavian Capitals</li><li>Scandinavia Cruise Packages</li><li>Exclusive Tours</li><li>Midnight Sun</li></ul></div>
    <div class="col" style="left:819px;top:24px"><ul><li>Activity Tours</li><li>Meet the locals</li><li>Northern lights</li><li>Norway Tours</li><li>Sweden Tours</li><li>Iceland Tours</li></ul></div>

    <div class="col" style="left:20px;top:200px"><h4>Recently Added Tours</h4><ul><li>Baltic &amp; Russian Explorer</li><li>Iceland Wilderness</li><li>Baltic Classical</li></ul></div>
    <div class="col" style="left:200px;top:200px"><h4>Recently Added Tours</h4><ul><li>Norway Winter Cruises</li><li>Snow Lodge Holidays</li><li>Winter Rail Tours</li></ul></div>
    <div class="col" style="left:376px;top:200px"><ul><li>Lapland Winter Tours</li><li>Winter Weekend Breaks</li><li>Winter Tours Unpolished</li></ul></div>
    <div class="col" style="left:620px;top:200px"><h4>Brightfell Journeys</h4><ul><li>About Brightfell Journeys</li><li>Booking and Payment Procedure</li><li>Terms and Conditions</li></ul></div>
    <div class="col" style="left:819px;top:200px"><ul><li>Frequently Asked Questions (FAQ)</li><li>Travel Experiences</li><li>Photo Credits</li><li>Site Map</li><li>Contact</li></ul></div>
  </footer>

  <div class="abs copy">© 2015 Brightfell Journeys AS</div>
  <div class="abs pay" style="left:472px;width:46px;background:#1a3f8f"></div>
  <div class="abs pay" style="left:524px;width:44px;background:#d8dde8"></div>
  <div class="abs pay" style="left:575px;width:44px;background:#e7a22a"></div>
  <div class="abs pay" style="left:626px;width:42px;background:#e6d7c6"></div>
  <div class="abs social"></div>

</div>
</body>
</html>
```